Flyer Design Project

I require a double sided flyer in PSD format.
The flyer should look fresh and clean.
The flyer is for an digital marketing company that offers various services. The services are broken down into 3 main categories and the design should reflect this.
All the content is provided in the attached file
Industry/Entity Type
Digital
Requirements
Must have
- Front of the leaflet to be mainly white background with appealing text based questions in the colours in large font with relevant images.
Back if the
3 separate boxes using the colours indicated in the attachment for the services on back of the leafet.
Should not have
- Gradients
Borders on the edges of the design
Vignettes
Black elements
Any text below 10pt
Fancy fonts
Do not use old-style fonts

```html
<!DOCTYPE html>
<html lang="en">
<head>
<meta charset="utf-8">
<title>Digital Marketing Flyer – Front and Back</title>
<link rel="stylesheet" href="https://fonts.googleapis.com/css2?family=Quicksand:wght@400;500;600;700&display=swap">
<style>
  :root{
    --green:#8dc63f;
    --green-dark:#0f9a48;
    --blue:#3ec0e2;
    --blue-dark:#1f6fb8;
    --orange:#f47f20;
    --orange-dark:#e0691f;
    --white:#ffffff;
    --stage:#ecebe8;
  }
  *{box-sizing:border-box;margin:0;padding:0}
  html,body{width:1200px;height:1000px;overflow:hidden}
  body{background:var(--stage);font-family:"Quicksand",sans-serif;position:relative}

  .flyer{position:absolute;top:110px;width:540px;height:780px;background:var(--white);overflow:hidden;box-shadow:0 4px 18px rgba(60,50,40,.18)}
  .flyer--back{left:30px}
  .flyer--front{left:630px}

  /* ---------- Back: service bands ---------- */
  .bands{position:absolute;left:0;top:0}
  .band-content{position:absolute;left:30px;color:var(--white);font-size:20px;font-weight:500;line-height:26px}
  .band-content ul{list-style:none}
  .band-content li::before{content:"• "}
  .band-content b{font-weight:700}
  .band-content--consulting{top:30px}
  .band-content--design{top:262px}
  .band-content--sem{top:482px}

  .cta{position:absolute;left:36px;width:390px;height:62px;border:2px dashed rgba(255,255,255,.85);color:var(--white);text-align:center;font-weight:700;font-size:21px;line-height:25px;padding-top:5px}
  .cta em{font-style:normal;color:var(--orange)}
  .cta--consultation{top:150px;background:var(--green-dark)}
  .cta--website{top:384px;background:var(--blue-dark)}

  .discount{position:absolute;left:310px;top:556px;width:118px;height:118px;border-radius:50%;background:var(--orange-dark);border:2px dashed rgba(255,255,255,.85);color:var(--white);text-align:center;font-weight:700;padding-top:38px}
  .discount strong{display:block;font-size:20px;line-height:22px}
  .discount span{display:block;font-size:11px;line-height:13px}

  .service-label{position:absolute;right:8px;writing-mode:vertical-rl;color:var(--orange);font-size:16px;line-height:18px;text-transform:uppercase;letter-spacing:.5px}
  .service-label b{display:block;font-weight:700}
  .service-label span{display:block;font-weight:500}
  .service-label--consulting{top:62px}
  .service-label--design{top:310px}
  .service-label--sem{top:545px}

  .back-footer{position:absolute;left:30px;top:718px;color:var(--orange);font-size:13px;font-weight:700;line-height:20px}
  .back-footer .call{font-size:15px;font-weight:500}
  .back-footer .call b{font-weight:700}
  .pin{display:inline-block;vertical-align:-2px;margin-right:4px}

  .logo-box{position:absolute;background:var(--blue);color:var(--white);text-align:center;font-weight:700}
  .logo-box--small{left:430px;top:722px;width:96px;height:36px;font-size:13px;line-height:15px;padding-top:3px}
  .logo-box--small span{font-weight:500}

  /* ---------- Front: questions ---------- */
  .q{position:absolute;text-transform:uppercase;white-space:nowrap}
  .green{color:var(--green)}
  .orange{color:var(--orange)}
  .q-know{top:40px;left:60px;font-size:26px;line-height:30px;font-weight:500}
  .q-stat{top:64px;left:46px;font-size:120px;font-weight:700;line-height:110px;color:var(--orange);letter-spacing:-4px}
  .q-stat small{font-size:30px;letter-spacing:0}
  .stat-arrow{position:absolute;left:262px;top:76px}
  .q-consumers{top:182px;left:44px;font-size:26px;font-weight:500;line-height:32px}
  .q-consumers b{font-weight:700}

  .rule{position:absolute;left:0;height:2px;background:var(--orange)}
  .rule::before{content:"";position:absolute;left:0;top:-2px;width:60px;height:6px;background:var(--orange)}
  .rule--1{top:260px;width:520px}
  .rule--2{top:366px;width:530px}
  .rule--3{top:640px;width:510px}

  .q-finding{top:278px;left:50px;font-size:30px;font-weight:500;line-height:36px}
  .q-finding b{font-weight:700}
  .q-need{top:380px;left:56px;font-size:26px;line-height:30px;font-weight:500;letter-spacing:9px}
  .q-more{top:406px;left:44px;font-size:118px;font-weight:700;line-height:104px;letter-spacing:-2px;color:var(--green)}
  .q-customers{top:508px;left:48px;font-size:54px;font-weight:500;line-height:58px;color:var(--orange)}
  .q-business{top:566px;left:50px;font-size:28px;line-height:32px;font-weight:500;color:var(--green)}
  .q-help{position:absolute;top:610px;left:50px;font-size:16px;line-height:20px;font-weight:700;color:var(--orange)}

  .front-wave{position:absolute;left:0;bottom:0}
  .logo-box--large{left:310px;top:664px;width:180px;height:70px;font-size:28px;line-height:28px;padding-top:7px}
  .logo-box--large span{font-weight:500}
  .front-call{position:absolute;left:28px;bottom:18px;color:var(--white);font-size:17px;font-weight:500}
  .front-call b{font-weight:700}
</style>
</head>
<body>

<!-- Back side: services -->
<section class="flyer flyer--back" aria-label="Flyer back – services">
  <svg class="bands" width="540" height="780" viewBox="0 0 540 780" aria-hidden="true">
    <path d="M0 0 H540 C440 40 440 200 540 240 H0 Z" fill="#8dc63f"/>
    <path d="M0 240 H540 C440 285 440 425 540 470 H0 Z" fill="#3ec0e2"/>
    <path d="M0 470 H540 C440 515 440 655 540 700 H0 Z" fill="#f47f20"/>
  </svg>

  <div class="band-content band-content--consulting">
    <ul>
      <li>Marketing <b>strategy</b> and <b>planning</b></li>
      <li>Business <b>branding</b></li>
      <li>Competition <b>analysis</b>,</li>
    </ul>
  </div>
  <div class="cta cta--consultation">GET<br><em>FREE</em> CONSULTATION</div>
  <div class="service-label service-label--consulting"><b>Consulting</b><span>Services</span></div>

  <div class="band-content band-content--design">
    <ul>
      <li>Web Design</li>
      <li>Website maintenance</li>
      <li>Logo design</li>
      <li>Flyer design</li>
    </ul>
  </div>
  <div class="cta cta--website">GET<br><em>FREE</em> WEBSITE</div>
  <div class="service-label service-label--design"><b>Design</b><span>Services</span></div>

  <div class="band-content band-content--sem">
    <ul>
      <li>Local Business Marketing</li>
      <li>PPC</li>
      <li>Email marketing</li>
      <li>SEO</li>
      <li>Social media</li>
      <li>Content development</li>
      <li>Website audit</li>
      <li>Lead generation</li>
    </ul>
  </div>
  <div class="discount"><strong>25% OFF</strong><span>any SEM Package</span></div>
  <div class="service-label service-label--sem"><b>SEM</b><span>Services</span></div>

  <div class="back-footer">
    <div><svg class="pin" width="11" height="14" viewBox="0 0 11 14" aria-hidden="true"><path d="M5.5 0A5.5 5.5 0 0 0 0 5.5C0 9.6 5.5 14 5.5 14S11 9.6 11 5.5A5.5 5.5 0 0 0 5.5 0Zm0 7.6a2.1 2.1 0 1 1 0-4.2 2.1 2.1 0 0 1 0 4.2Z" fill="#f47f20"/></svg>Kestrel House, 14 Marlow Street, Birmingham, B3 4QR</div>
    <div class="call">Call <b>0121 555 0148</b> for a <b>FREE</b></div>
  </div>
  <div class="logo-box logo-box--small">LOGO<br><span>HERE</span></div>
</section>

<!-- Front side: questions -->
<section class="flyer flyer--front" aria-label="Flyer front – questions">
  <div class="q q-know green">Did you know</div>
  <div class="q q-stat">85<small>%</small></div>
  <svg class="stat-arrow" width="40" height="100" viewBox="0 0 40 100" aria-hidden="true">
    <line x1="20" y1="0" x2="20" y2="94" stroke="#8dc63f" stroke-width="4"/>
    <polyline points="5,78 20,96 35,78" fill="none" stroke="#8dc63f" stroke-width="4"/>
  </svg>
  <div class="q q-consumers green">Of consumers use the internet<br>to find <b class="orange">business</b> like yours ?</div>

  <div class="rule rule--1"></div>
  <div class="q q-finding green">Are your customers<br><b class="orange">Finding you</b> online ?</div>
  <div class="rule rule--2"></div>

  <div class="q q-need green">Do you need</div>
  <div class="q q-more">MORE</div>
  <div class="q q-customers">Customers</div>
  <div class="q q-business">For your business ?</div>
  <div class="q-help">Let us help you grow your business online</div>
  <div class="rule rule--3"></div>

  <svg class="front-wave" width="540" height="110" viewBox="0 0 540 110" aria-hidden="true">
    <path d="M0 30 C90 -6 170 8 260 34 C360 62 450 56 540 38 V110 H0 Z" fill="#3ec0e2"/>
  </svg>
  <div class="logo-box logo-box--large">LOGO<br><span>HERE</span></div>
  <div class="front-call">Call <b>0121 555 0148</b> for a <b>FREE</b></div>
</section>

</body>
</html>
```